Promotion for Local Garage - Orvale Motorworks offering 10% off

We are after an A5 Colour Leaflet to promote our business Orvale Motorworks.

Orvale Motorworks is a local garage and we are about to launch a flyer campaign in the local area.

Services we provide:
Servicing, Repairs, Diagnostics, Clutches, Brakes, Exhaust for all makes and models of cars and vans.

10% discount for anyone who brings in this flyer with them.

Company contact details below:
Telephone 0151 3846172
Website www.orvalemotorworks-example.co.uk

Address
Unit 4 Hollin Workshops,
Brackwell Lane,
Fenwick Ind Estate,
Ellesmere Port,
CH64 9QP

Our Logo is attached

Target Market(s)

Local Residents and businesses

Industry/Entity Type

Auto Repair

Requirements
Must have
• Services we provide:
• Servicing, Repairs, Diagnostics, Clutches, Brakes, Exhaust for all makes and models of cars and vans.
• 10% discount for anyone who brings in this flyer with them.
• Company contact details below:
• Telephone 0151 3846172
• Website www.orvalemotorworks-example.co.uk
• Address
• Unit 4 Hollin Workshops,
• Brackwell Lane,
• Fenwick Ind Estate,
• Ellesmere Port,
• CH64 9QP

```html
<!DOCTYPE html>
<html lang="en">
<head>
<meta charset="utf-8">
<title>Orvale Motorworks – A5 Leaflet</title>
<link rel="stylesheet" href="https://fonts.googleapis.com/css2?family=Lato:wght@400;700;900&display=swap">
<style>
  :root {
    --red: #e8232a;
    --dark: #2e3135;
    --ink: #3a3a3a;
    --yellow: #ffe100;
    --white: #ffffff;
    --stage: #a9a9a9;
  }
  * { box-sizing: border-box; margin: 0; padding: 0; }
  html, body { width: 1200px; height: 561px; overflow: hidden; }
  body { background: var(--stage); font-family: "Lato", Arial, sans-serif; position: relative; }

  .leaflet-frame { position: absolute; left: 405px; top: 0; width: 390px; height: 561px; overflow: hidden; }
  .leaflet { position: absolute; left: 0; top: 0; width: 487px; height: 701px; transform: scale(0.8); transform-origin: 0 0; background: var(--dark); overflow: hidden; }

  .photo-hero { position: absolute; left: 0; top: 0; width: 487px; height: 300px;
    background: linear-gradient(100deg, #2b3446 0%, #34405a 28%, #8c8f96 45%, #b9b7b3 62%, #6c6e72 85%, #4a4c50 100%); }
  .photo-workshop { position: absolute; left: 240px; top: 352px; width: 256px; height: 256px; border-radius: 50%;
    border: 6px solid var(--white); box-shadow: 0 3px 8px rgba(0,0,0,.35);
    background: radial-gradient(circle at 60% 30%, #5f93c9 0%, #3f6fa8 25%, #c9c9c6 50%, #8e8e8c 80%, #5c5c5c 100%); }

  .shapes { position: absolute; left: 0; top: 0; width: 487px; height: 701px; }

  .brand { position: absolute; left: 276px; top: 60px; font-size: 21px; font-weight: 700; color: var(--ink); letter-spacing: .2px; white-space: nowrap; }

  .discount { position: absolute; left: 5px; top: 250px; width: 140px; text-align: center; color: var(--red); font-weight: 900; transform: rotate(-18deg); line-height: .9; }
  .discount-value { display: block; font-size: 46px; }
  .discount-label { display: block; font-size: 19px; }

  .offer { position: absolute; left: 163px; top: 302px; color: var(--white); font-size: 20px; font-weight: 700; line-height: 1.15; }

  .services { position: absolute; left: 13px; top: 400px; }
  .services-title { color: var(--yellow); font-size: 17.5px; font-weight: 900; margin-bottom: 4px; }
  .services-list { list-style: none; color: var(--white); font-size: 16px; line-height: 22px; margin-left: 12px; }
  .services-list li { position: relative; padding-left: 14px; }
  .services-list li::before { content: ""; position: absolute; left: 0; top: 8px; width: 6px; height: 6px; border-radius: 50%; background: var(--yellow); }
  .services-list .wrap { line-height: 16px; padding-top: 3px; }
  .services-list .wrap::before { top: 8px; }

  .contact { position: absolute; left: 13px; top: 592px; font-style: normal; }
  .contact-row { display: flex; align-items: center; gap: 8px; }
  .contact-phone { color: var(--red); font-size: 19px; font-weight: 900; }
  .contact-address { color: var(--ink); font-size: 12px; line-height: 12.5px; margin-top: 5px; }
  .icon { width: 18px; height: 18px; flex: none; fill: #555; }

  .website { position: absolute; left: 0; top: 660px; width: 487px; height: 41px; display: flex; align-items: center; justify-content: center;
    color: var(--yellow); font-size: 17px; font-weight: 900; letter-spacing: 1.6px; white-space: nowrap; }
</style>
</head>
<body>
  <div class="leaflet-frame">
    <article class="leaflet">
      <div class="photo-hero" role="img" aria-label="Mechanic holding a diagnostic tablet in a garage workshop"></div>

      <svg class="shapes" viewBox="0 0 487 701" aria-hidden="true">
        <path d="M0,290 Q260,262 487,165 L487,385 L0,385 Z" fill="var(--dark)"/>
        <path d="M0,255 Q260,236 487,130 L487,165 Q260,262 0,290 Z" fill="var(--red)"/>
        <circle cx="372" cy="28" r="112" fill="var(--white)" stroke="var(--red)" stroke-width="7"/>
        <rect x="0" y="385" width="487" height="195" fill="var(--red)"/>
        <defs>
          <linearGradient id="contactBand" x1="0" x2="1">
            <stop offset="0" stop-color="#d9d9d9"/><stop offset="1" stop-color="#f3f3f3"/>
          </linearGradient>
        </defs>
        <rect x="0" y="580" width="487" height="80" fill="url(#contactBand)"/>
        <rect x="0" y="660" width="487" height="41" fill="var(--red)"/>
        <polygon fill="var(--white)" points="147,290 133.9,301.7 141.5,317.6 124.9,323.4 125.9,340.9 108.4,339.9 102.6,356.5 86.7,348.9 75,362 63.3,348.9 47.4,356.5 41.6,339.9 24.1,340.9 25.1,323.4 8.5,317.6 16.1,301.7 3,290 16.1,278.3 8.5,262.4 25.1,256.6 24.1,239.1 41.6,240.1 47.4,223.5 63.3,231.1 75,218 86.7,231.1 102.6,223.5 108.4,240.1 125.9,239.1 124.9,256.6 141.5,262.4 133.9,278.3"/>
      </svg>

      <div class="photo-workshop" role="img" aria-label="Blue cars raised on lifts in a garage workshop"></div>

      <div class="brand">Orvale Motorworks</div>

      <div class="discount"><span class="discount-value">10%</span><span class="discount-label">DISCOUNT</span></div>

      <p class="offer">For anyone who brings in<br>this flyer with them.</p>

      <section class="services">
        <h2 class="services-title">SERVICES WE PROVIDE:</h2>
        <ul class="services-list">
          <li>Servicing</li>
          <li>Repairs</li>
          <li>Diagnostics</li>
          <li>Clutches</li>
          <li>Brakes</li>
          <li class="wrap">Exhaust for all makes and<br>models of cars and vans.</li>
        </ul>
      </section>

      <address class="contact">
        <div class="contact-row">
          <svg class="icon" viewBox="0 0 24 24" aria-hidden="true"><path d="M6.6 10.8a15.1 15.1 0 0 0 6.6 6.6l2.2-2.2a1 1 0 0 1 1-.25 11.4 11.4 0 0 0 3.6.6 1 1 0 0 1 1 1V20a1 1 0 0 1-1 1A17 17 0 0 1 3 4a1 1 0 0 1 1-1h3.5a1 1 0 0 1 1 1c0 1.25.2 2.45.6 3.6a1 1 0 0 1-.25 1z"/></svg>
          <span class="contact-phone">0151 3846172</span>
        </div>
        <div class="contact-row">
          <svg class="icon" viewBox="0 0 24 24" aria-hidden="true"><path d="M12 2a7 7 0 0 0-7 7c0 5.2 7 13 7 13s7-7.8 7-13a7 7 0 0 0-7-7zm0 9.5A2.5 2.5 0 1 1 12 6.5a2.5 2.5 0 0 1 0 5z"/></svg>
          <p class="contact-address">Unit 4 Hollin Workshops, Brackwell Lane,<br>Fenwick Ind Estate, Ellesmere Port, CH64 9QP</p>
        </div>
      </address>

      <div class="website">www.orvalemotorworks-example.co.uk</div>
    </article>
  </div>
</body>
</html>
```